Business Cards, Letterheads, Envelopes

A company's new identity to be reflected on its stationery items

Target Market(s)

Large Corporate Companies & Enterprises

Font styles to use
Sans Serif

Colors
0555a3
3176b5
85abd2
85cae6
33a6d7
0293ce

```html
<!DOCTYPE html>
<html lang="en">
<head>
<meta charset="utf-8">
<title>Corvane Systems Stationery</title>
<link rel="stylesheet" href="https://fonts.googleapis.com/css2?family=Questrial&family=Roboto:wght@400;500&display=swap">
<style>
:root{
  --blue:#3176b5;
  --brand:#3589c9;
  --ink:#222;
  --grey:#666;
  --paper:#f0f0f0;
  --paper-light:#f7f7f7;
  --dark:#1e1e1e;
  --bg:#dcdcdc;
}
*{margin:0;padding:0;box-sizing:border-box}
html,body{width:1200px;height:1200px;overflow:hidden;background:var(--bg)}
.canvas{position:relative;width:1200px;height:1200px;font-family:'Roboto',sans-serif}
.piece{position:absolute;overflow:hidden}
.brand{display:flex;align-items:center;gap:8px;font-family:'Questrial',sans-serif;color:var(--brand);white-space:nowrap}
.brand-dot{border-radius:50%;background:var(--brand);flex:none}

/* letterhead */
.letterhead{left:53px;top:219px;width:552px;height:777px;background:var(--paper)}
.letterhead .brand{position:absolute;left:51px;top:70px;font-size:17px}
.letterhead .brand-dot{width:34px;height:34px}
.sender{position:absolute;left:412px;top:52px;font-size:8.2px;line-height:12px;color:var(--ink)}
.sender .name{color:var(--brand)}
.letter{position:absolute;left:51px;top:218px;width:447px;font-family:'Questrial',sans-serif;color:var(--grey)}
.salutation{font-size:14px;color:#555;margin-bottom:22px}
.letter p{font-size:8.4px;line-height:11.9px;text-align:justify;margin-bottom:11.8px}
.closing{font-size:8.4px;margin-top:22px}
.signature{display:block;width:100px;height:42px;margin-top:14px;margin-left:-6px;background:linear-gradient(90deg,#dfe6ee,#cad8e8)}
.footer-band{position:absolute;left:0;top:741px;width:552px;height:16px;background:var(--brand)}
.footer-band .contacts{display:flex;gap:34px;padding-left:51px;line-height:16px;font-size:9.4px;color:#fff}
.footer-mark{position:absolute;left:456px;top:730px;width:40px;height:40px;border-radius:50%;background:var(--paper);border:2px solid var(--brand)}
.contact{display:inline-flex;align-items:center;gap:3px}
.contact svg{width:8px;height:8px}

/* business cards */
.card-front{left:615px;top:221px;width:272px;height:163px;background:#fff}
.card-deco{position:absolute;left:140px;top:-20px;width:150px;height:150px;border-radius:50%;background:radial-gradient(circle,#f6f6f6,#efefef)}
.holder{position:absolute;left:16px;top:20px}
.holder .person{font-size:9.6px;color:var(--brand);font-weight:500}
.holder .role{font-size:5.6px;color:var(--ink);margin-top:2px}
.card-info{position:absolute;left:16px;top:92px;font-size:5.6px;line-height:8.6px;color:var(--ink)}
.card-info .name{color:var(--brand)}
.card-info .lines{margin-top:9px;font-size:6.2px;line-height:9px}
.card-info svg{width:5px;height:5px}
.card-front .brand{position:absolute;left:134px;top:120px;font-size:8.6px;gap:5px}
.card-front .brand-dot{width:16px;height:16px}
.card-back{left:899px;top:221px;width:271px;height:163px;background:linear-gradient(110deg,#2a2a2a,var(--dark))}
.card-back .brand{position:absolute;left:48px;top:73px;font-size:12.5px}
.card-back .brand-dot{width:22px;height:22px}

/* envelope back */
.env-back{left:614px;top:433px;width:556px;height:252px;background:var(--paper-light)}
.flap{position:absolute;left:0;top:0}
.flap-dot{position:absolute;left:262px;top:20px;width:32px;height:32px;border-radius:50%;background:#fff}

/* envelope front */
.env-front{left:614px;top:738px;width:557px;height:255px;background:var(--paper-light)}
.env-front .brand{position:absolute;left:31px;top:31px;font-size:14.5px}
.env-front .brand-dot{width:30px;height:30px}
.env-address{position:absolute;left:31px;top:206px;font-size:8px;line-height:12px;color:var(--ink)}
.env-address .name{color:var(--brand)}
.env-address .lines{display:flex;gap:10px}
.env-address svg{width:7px;height:7px}
.env-band{position:absolute;left:0;top:230px;width:557px;height:9px;background:var(--brand)}
.env-mark{position:absolute;left:497px;top:218px;width:34px;height:34px;border-radius:50%;background:var(--paper-light);border:2px solid var(--brand)}
</style>
</head>
<body>
<div class="canvas">

  <section class="piece letterhead">
    <div class="brand"><span class="brand-dot"></span>CORVANE SYSTEMS</div>
    <div class="sender">
      <div class="name">Corvane Systems Pvt. Ltd</div>
      <div>480 Linden Avenue NY.</div>
      <div>Westbrook AB TIR</div>
    </div>
    <div class="letter">
      <div class="salutation">Dear Mr. Brennan,</div>
      <p>Lorem ipsum dolor sit amet, consectetur adipiscing elit. Donec orci purus, luctus vitae dignissim eu, iaculis sed purus. Vivamus faucibus, ipsum nec aliquet viverra, leo mauris condimentum ligula, sit amet sagittis enim ligula quis arcu. Nam egestas tortor id nisi porttitor mattis. In tortor ante, ultricies in suscipit a, tempus non massa. Vivamus et auctor mi. Fusce vel massa nulla. Phasellus nec eros mauris, et scelerisque orci.</p>
      <p>Donec malesuada orci vitae nulla accumsan porta a id massa. Quisque accumsan iaculis magna sit amet fringilla. Maecenas consequat, magna eget tincidunt semper, odio nibh rutrum mi, id feugiat ante nisi eu risus. Vestibulum nunc orci, rhoncus a placerat in, ultricies in mi. Cras mattis varius eros, vel fringilla nisi suscipit eget. Quisque scelerisque sagittis nulla at porttitor.</p>
      <p>Sed id augue vitae urna euismod commodo aliquet a quam. Pellentesque arcu velit, cursus et malesuada ut, consequat et diam. Nullam erat sem, rhoncus id ullamcorper vitae, rhoncus et arcu. In ultricies ultricies nulla, ut rutrum nisi iaculis at. Donec eu magna a metus ornare faucibus. Fusce aliquet faucibus ultricies. Morbi semper, est id tincidunt gravida, sem arcu adipiscing lacus, ac bibendum nulla leo eu purus. Quisque nec diam sed risus consectetur a ccumsan quis quis nibh. Vestibulum id purus lorem.</p>
      <p>It is a long established fact that a reader will be distracted by the readable content of a page when looking at its layout. The point of using Lorem Ipsum is that it has a more-or-less normal distribution of letters, as opposed to using 'Content here, content here', making it look like readable English. Many desktop publishing packages</p>
      <div class="closing">Sincerely,</div>
      <span class="signature" role="img" aria-label="Handwritten signature of Peter Harlow"></span>
    </div>
    <div class="footer-band">
      <div class="contacts">
        <span class="contact"><svg viewBox="0 0 10 10"><path d="M2 1l2 2-1 1.5c.8 1.4 1.6 2.2 3 3L7.5 6l2 2-1.5 1.5C4.5 9 1 5.5.5 2.5z" fill="#fff"/></svg>204880XX</span>
        <span class="contact"><svg viewBox="0 0 10 10"><rect x="1" y="2" width="8" height="6" fill="none" stroke="#fff"/><path d="M1 2l4 3 4-3" fill="none" stroke="#fff"/></svg>daniel@corvane.com</span>
        <span class="contact"><svg viewBox="0 0 10 10"><circle cx="5" cy="5" r="4" fill="none" stroke="#fff"/><path d="M1 5h8M5 1c-2 2.5-2 5.5 0 8M5 1c2 2.5 2 5.5 0 8" fill="none" stroke="#fff" stroke-width=".7"/></svg>www.corvane.com</span>
      </div>
    </div>
    <div class="footer-mark"></div>
  </section>

  <section class="piece card-front">
    <div class="card-deco"></div>
    <div class="holder">
      <div class="person">DANIEL MARSH</div>
      <div class="role">Managing Director</div>
    </div>
    <div class="card-info">
      <div class="name">Corvane Systems Pvt. Ltd</div>
      <div>480 Linden Avenue NY.</div>
      <div>Westbrook AB TIR</div>
      <div class="lines">
        <div class="contact"><svg viewBox="0 0 10 10"><path d="M2 1l2 2-1 1.5c.8 1.4 1.6 2.2 3 3L7.5 6l2 2-1.5 1.5C4.5 9 1 5.5.5 2.5z" fill="#3589c9"/></svg>204880XX</div><br>
        <div class="contact"><svg viewBox="0 0 10 10"><rect x="1" y="2" width="8" height="6" fill="#3589c9"/></svg>daniel@corvane.com</div><br>
        <div class="contact"><svg viewBox="0 0 10 10"><circle cx="5" cy="5" r="4" fill="#3589c9"/></svg>www.corvane.com</div>
      </div>
    </div>
    <div class="brand"><span class="brand-dot"></span>CORVANE SYSTEMS</div>
  </section>

  <section class="piece card-back">
    <div class="brand"><span class="brand-dot"></span>CORVANE SYSTEMS</div>
  </section>

  <section class="piece env-back">
    <svg class="flap" width="556" height="80" viewBox="0 0 556 80"><path d="M0 0H556L548 30Q538 80 500 80H56Q18 80 8 30Z" fill="#3589c9"/></svg>
    <div class="flap-dot"></div>
  </section>

  <section class="piece env-front">
    <div class="brand"><span class="brand-dot"></span>CORVANE SYSTEMS</div>
    <div class="env-address">
      <div><span class="name">Corvane Systems Pvt. Ltd</span>&nbsp; 480 Linden Avenue NY. Westbrook AB TIR</div>
      <div class="lines">
        <span class="contact"><svg viewBox="0 0 10 10"><path d="M2 1l2 2-1 1.5c.8 1.4 1.6 2.2 3 3L7.5 6l2 2-1.5 1.5C4.5 9 1 5.5.5 2.5z" fill="#3589c9"/></svg>204880XX</span>
        <span class="contact"><svg viewBox="0 0 10 10"><rect x="1" y="2" width="8" height="6" fill="#3589c9"/></svg>daniel@corvane.com</span>
        <span class="contact"><svg viewBox="0 0 10 10"><circle cx="5" cy="5" r="4" fill="#3589c9"/></svg>www.corvane.com</span>
      </div>
    </div>
    <div class="env-band"></div>
    <div class="env-mark"></div>
  </section>

</div>
</body>
</html>
```